For Sale Poster Design

We need a beautiful and tropical looking FOR SALE poster for our speed boat.

Poster format need to be 297x420mm / 300dpi
PSD with all layers.

The photos from the boat can be downloaded here: www.korvado.nl/photos.zip

Target Market(s)

Tourists, expats

Requirements
Must have
• The poster need to have the following text:

Speed Boat Sale

This beautiful full glass fiber speedboat (location Lombok, Indonesia) is perfect for tropical conditions: island transfer, diving, wake boarding, fishing, private charters and leisure activities.

The newly bought 2x 200 HP TORUMI 4 Stroke (2013) will give you an enormous power on the water with maximum speed of 40 Knot / 74 Km/hour. This will bring you from Lombok to Bali in just 50 minutes and only few minutes long from the famous tropical Gili islands.

The speedboat also has the comfort of a small cabin with skylight, sun controlled ventilation system, a small bed, a toilet and a fridge. There are 16 seats in the open section of the boat. The boat is equipped with modern brand-new GPS, Sonar and an FM / AM Radio system.

This speedboat was built in 2011 and is meticulously maintained to the highest standard. It comes with a captain and boatman.

Specs:
Overall length: 11 Meter 36 feet.
Built year: 2011, Bali
Engines: 2x 200 HP TORUMI 4 Stroke (Bought 2013)
Capacity: Max. 16 People (Incl. Crew)
Max speed: 40 Knot / 74 Km/hour
GPS / Sonar: Pelcorn RM-42TX
Tankage: 300 Liter
Lighting: LED / Halogen

Price 99.000 USD
Nice to have
• Big FOR SALE banner on the poster

```html
<!DOCTYPE html>
<html lang="en">
<head>
<meta charset="utf-8">
<title>Speed Boat For Sale Poster</title>
<link rel="stylesheet" href="https://fonts.googleapis.com/css2?family=Poppins:wght@700&family=Questrial&family=Oswald:wght@500;600&display=swap">
<style>
  :root {
    --stage: #000000;
    --sky-top: #1f63c0;
    --sky-mid: #3a8ad6;
    --sky-light: #7fb9e8;
    --sea-deep: #0f4f8e;
    --sea-light: #3b93c9;
    --title-navy: #0d1b4d;
    --text-white: #ffffff;
    --text-shadow: #0a2a5c;
    --price-red: #e4161b;
    --frame-brown: #6a4418;
    --cabin-cream: #e9dfc9;
    --cabin-white: #f4f6f7;
    --hull-white: #eef1f3;
  }
  * { margin: 0; padding: 0; box-sizing: border-box; }
  html, body {
    width: 789px; height: 1200px; overflow: hidden;
    background: var(--stage);
  }
  .poster {
    position: absolute; left: 71px; top: 40px;
    width: 650px; height: 920px; overflow: hidden;
    font-family: "Questrial", "Century Gothic", sans-serif;
    color: var(--text-white);
  }
  .poster__backdrop {
    position: absolute; inset: 0;
    background: linear-gradient(180deg,
      var(--sky-top) 0%, var(--sky-mid) 28%, var(--sky-mid) 50%,
      var(--sky-light) 62%, var(--sea-light) 68%, var(--sea-deep) 78%, var(--sea-light) 100%);
  }
  .poster__title {
    position: absolute; top: 18px; left: 0; width: 100%;
    text-align: center;
    font-family: "Poppins", "Century Gothic", sans-serif;
    font-weight: 700; font-size: 98px; line-height: 1; letter-spacing: 3px;
    color: var(--title-navy);
    text-shadow: 0 0 12px rgba(255,255,255,.55), 0 2px 2px rgba(255,255,255,.4);
  }
  .copy {
    position: absolute; left: 46px; top: 124px; width: 558px;
    font-size: 15.5px; line-height: 21.3px; text-align: justify;
    text-shadow: 0 0 2px var(--text-shadow), 1px 1px 1px var(--text-shadow);
  }
  .copy__heading, .specs__heading {
    font-family: "Poppins", sans-serif; font-weight: 700;
    font-size: 19px; line-height: 22px; text-transform: uppercase;
  }
  .copy p { margin-bottom: 8px; }
  .specs {
    position: absolute; left: 46px; top: 458px; font-size: 13.5px; line-height: 16.7px;
    text-shadow: 0 0 2px var(--text-shadow), 1px 1px 1px var(--text-shadow);
  }
  .specs__heading { margin-bottom: 2px; }
  .specs__row { display: flex; white-space: nowrap; }
  .specs__label { width: 93px; }
  .price {
    position: absolute; left: 300px; top: 580px; width: 304px; text-align: right;
    font-family: "Oswald", sans-serif; font-weight: 500; color: var(--price-red);
    font-size: 19px; line-height: 34px; white-space: nowrap;
  }
  .price__amount { font-weight: 600; font-size: 33px; vertical-align: -2px; }
  .gallery {
    position: absolute; left: 41px; top: 629px; width: 569px; height: 160px;
    background: var(--frame-brown); padding: 6px; display: flex; gap: 6px;
  }
  .gallery__photo { height: 100%;
    background: linear-gradient(180deg, var(--cabin-white) 0%, #dfe6ea 45%, var(--cabin-cream) 70%, #cfc3a8 100%); }
  .gallery__photo--wide { flex: 0 0 222px; }
  .gallery__photo--narrow { flex: 1 1 auto; }
  .hero-boat {
    position: absolute; left: 75px; top: 790px; width: 390px; height: 130px;
    background: linear-gradient(180deg, #8fc2e6 0%, var(--hull-white) 40%, #d9e1e6 70%, #2a5f8c 100%);
  }
</style>
</head>
<body>
  <main class="poster">
    <div class="poster__backdrop" role="img" aria-label="Tropical blue sky with clouds over calm open sea"></div>
    <h1 class="poster__title">FOR SALE</h1>

    <section class="copy">
      <h2 class="copy__heading">Speed Boat Sale</h2>
      <p>This beautiful full glass fiber speed boat (location Lombok, Indonesia) is perfect for tropical conditions, Island transfer, diving, wake boarding, fishing, private charters and leisure features.</p>
      <p>The new (2013) bought 2 x 200 HP TORUMI 4 Stroke will give you an enormous power on the water with maximum speed of 40 Knot / 74 Km/hour and will bring you within only 50 minutes from Lombok to Bali and within minute distance from all famous tropical Gili islands.</p>
      <p>The speed boat also has the comfort of a small cabin with skylight, sun controlled ventilation system, a small bed, a toilet and a fridge. In the open section of the boat are 16 seats, besides all of this is the boat equipped with brand-new GPS, Sonar and an FM / AM Radio system.</p>
      <p>This boat was built in 2011 and it was meticulously maintained to the highest standard.</p>
    </section>

    <section class="specs">
      <h2 class="specs__heading">Specs :</h2>
      <div class="specs__row"><span class="specs__label">Overall length</span><span>: 11 Meter 36 feet.</span></div>
      <div class="specs__row"><span class="specs__label">Built year</span><span>: 2011, Bali</span></div>
      <div class="specs__row"><span class="specs__label">Engines</span><span>: 2 x 200 HP TORUMI 4 Stroke (Bought 2013)</span></div>
      <div class="specs__row"><span class="specs__label">Capacity</span><span>: Max. 16 People (Incl. Crew)</span></div>
      <div class="specs__row"><span class="specs__label">Max speed</span><span>: 40 Knot / 74 Km/hour</span></div>
      <div class="specs__row"><span class="specs__label">GPS / Sonar</span><span>: Pelcorn RM-42TX</span></div>
      <div class="specs__row"><span class="specs__label">Tankage</span><span>: 300 Liter</span></div>
      <div class="specs__row"><span class="specs__label">Lighting</span><span>: LED / Halogen</span></div>
    </section>

    <p class="price">BEST PRICE <span class="price__amount">99.000</span> USD ONLY</p>

    <div class="gallery">
      <div class="gallery__photo gallery__photo--wide" role="img" aria-label="Boat cabin interior with cream bench seats and helm"></div>
      <div class="gallery__photo gallery__photo--narrow" role="img" aria-label="Cabin storage nook with coiled rope"></div>
      <div class="gallery__photo gallery__photo--wide" role="img" aria-label="Cabin seating row beside large side windows"></div>
    </div>

    <div class="hero-boat" role="img" aria-label="White speed boat with twin outboard engines cruising on the sea"></div>
  </main>
</body>
</html>
```